Corporate website design needed

We need a Contemporary Industrial/Tech/Logistics Website design to match our logistic client's business. Our client consults and build logistics solutions that they manage but they are not a typical 3PL (3rd party logistics company) which is primarily engaged in moving boxes.
PSD file only for now, home and default templates.
COMPANY CHARACTER
DESIGN LOOK AND FEEL
• The design should also be modern and visually well organized — employing a combination of visual devices and info graphics. Keep it light and not too heavy but strong/ professional. And unique.
• The design should go beyond the typical industrial pick and pack 3PL representing [Logistics Company] as a High Tech/IT logistics company.
Some examples although these are not right for this client because they have much more content and present themselves more as a 3pl.
http://www.tg-gateway.example/ (More right then wrong - Like this but simplified)
http://www.morvanfreight.example (Ugly)
http://www.pdwellstead.example (More right then wrong but different focus)
http://www.halverinco.example/ Too 3PL trucking… We want a bit ore high level approach
The difference, the design should be a fusion in core concepts that culminate in a design which implies the following attributes. Tech (Big data / analytics / software), Consultancy (Solutions, SME, Leader), 3PL Industry vertical solutions.
NOTE: The visualization of “tech” is not “1” and “0”, but more “software and analytics” Perhaps more like www.quantelyx.example.
• They need to be seen as a solutions provider in Logistics and as in Subject matter experts
TONE
The tone needs to exude professionalism, expertise, though leadership along with technical and executional excellence.
Experienced
Knowledgeable
Confident
Determined
Straightforward
WEBSITE OBJECTIVES
• Focus C-Suite executives and logistics managers’ attention on [Logistics Company]s commanding knowledge and expertise, and unique approach to supply chain solutions producing more RFP wins
• Create an easy to scan design which decreases the reliance on text through featured text, summaries, and smaller “chunked” size bits of information.
• Convey [Logistics Company] as high-tech 3PL solutions developer and services provider with a ‘high-touch’ consultative approach.
• Showcase [Logistics Company]’s value propositions. (See Slider Content)
• Showcase [Logistics Company]’s expertise in logistical analytics.
• Gain recognition as an industry leader in evolutionary new space (supply chain 2.0)
WEBSITE STRATEGY
• Reduce reliance on text (at least within initial entry points for each section)
• Typography: Watch text line lengths and readability, bolder fonts. NO SERIFS
• Generally, create a click-through format so that users who want more details can find it, and those who don’t can get a snapshot without clicking through.
• Increase visual content through info graphics and some dynamic content, photography
• Better utilize the space on each page (e.g., add visual interest, photography and iconography where appropriate to break up copy blocks and maintain readable line lengths).
COLOR SCHEME
• Create a more engaging color scheme (the logo will remain the same under all circumstances).
• Red / grayscale may work…. Not too dark or heavy. Not too much red. Ex. parvixa.example
• Also try blues and greys. They seem to like that. Open to suggestions but don’t get to crazy. Red is in their logo but too much may be a problem.
PHOTOGRAPHY
Yes. And I will upload some.
If you pick photography please be sure to note Which stock house used and the image number!
CONTENT
The content will be presented in a more hierarchical format — with lead-ins, paragraph and section headers and navigational cues to expand lengthier content allowing the visitor to more easily scan the website. No case studies, No Social media, News while on the home page should not be over emphasized. They don't post a lot so it gets dated quickly ...
I will be uploading a wire frame and other elements.
NOTE: I uploaded my EXAMPLE mock up which is close but not close enough.
I am not a great designer. So I am looking for an alternative that exceed my design ability! These examples show the basic layout but I really want some varied alternatives.
The colors are inconsistent and type not quite right. The grey bar at top is not right and should probably go away.
Please pull the basic elements in the example together into a great design.
If you have questions please contact me.
i will upload some photography tomorrow that may be of use.
Thanks!
Updates
Hi All,
We are still evaluating the submitted designs. Sorry for the delay.
Target Market(s)
This website is primarily a validation website. Few new customers will search and find them as such...
The site should be Focused on C-Suite executives and logistics managers’ attention on [Logistics Company]s commanding knowledge and expertise, and unique approach to supply chain solutions producing more RFP wins
Industry/Entity Type
Business
Requirements
Must have
- Slide show, Clearly explain who they are and what they do.
Create an easy to scan design which decreases the reliance on text through featured text, summaries, and smaller “chunked” size bits of information.
Convey [Logistics Company] as high-tech 3PL solutions developer and services
provider with a ‘high-touch’ consultative approach.
Should not have
- No Ads space
No Social media
Not too cluttered. Keep it clean.

```html
<!DOCTYPE html>
<html lang="en">
<head>
<meta charset="utf-8">
<title>Northbay Logistics</title>
<link rel="stylesheet" href="https://fonts.googleapis.com/css2?family=Open+Sans:wght@400;600;700&family=Arimo:wght@400;700&family=Oswald:wght@400&display=swap">
<style>
:root{
  --red:#c8102e;
  --nav:#4a4a4a;
  --light:#eeeeee;
  --white:#fff;
  --text:#444;
}
*{margin:0;padding:0;box-sizing:border-box}
html,body{width:1016px;height:1200px;overflow:hidden}
body{position:relative;background:var(--white);font-family:"Arimo",Arial,sans-serif;color:var(--text)}
.abs{position:absolute}

/* top nav */
.topbar{left:0;top:0;width:1016px;height:35px;background:var(--nav)}
.topbar a{position:absolute;top:12px;font:700 11px "Arimo",Arial,sans-serif;color:var(--white);text-decoration:none;white-space:nowrap}
.social{display:flex;gap:8px}
.social span{width:22px;height:22px;border-radius:50%;background:var(--white);display:block}
.topbar .social{position:absolute;left:750px;top:7px}

/* header */
.brand{display:flex;align-items:center;gap:12px}
.brand-mark{width:34px;height:34px;border-radius:50%;background:var(--red)}
.brand-name{font:600 14px "Open Sans",sans-serif;letter-spacing:5px;color:#333;line-height:1.25;white-space:nowrap}
.header-brand{left:88px;top:58px}
.phone{left:630px;top:62px;width:276px;height:34px;border-top:1px dotted #999;border-bottom:1px dotted #999;display:flex;align-items:center;gap:6px;white-space:nowrap}
.phone-label{font:400 15px "Oswald",sans-serif;color:#222}
.phone-number{font:400 20px "Oswald",sans-serif;color:var(--red)}

/* hero */
.hero-band{left:0;top:122px;width:1016px;height:320px;background:repeating-linear-gradient(45deg,#2c2c2c 0 2px,#353535 2px 4px)}
.hero-photo{left:86px;top:122px;width:620px;height:320px;background:linear-gradient(100deg,#dfe6df 0%,#f2f2f0 40%,#c9b69d 75%,#ebe8e3 100%)}
.tracking{left:706px;top:122px;width:224px;height:320px;background:linear-gradient(160deg,#dd3442,#c81e2e)}
.tracking h2{position:absolute;left:12px;top:10px;font:700 27px "Open Sans",sans-serif;color:var(--white);letter-spacing:.5px}
.tracking p{position:absolute;left:13px;top:52px;width:198px;font:400 11px/18.6px "Arimo",Arial,sans-serif;color:var(--white)}
.field{position:absolute;left:17px;width:189px;height:29px;background:var(--white);font:400 11px "Arimo",Arial,sans-serif;color:#777;padding:8px 9px}
.field svg{position:absolute;right:6px;top:10px}
.track-btn{position:absolute;left:120px;top:268px;width:84px;height:27px;background:linear-gradient(#333,#111);border-radius:3px;color:var(--white);font:400 12px "Arimo",Arial,sans-serif;text-align:center;line-height:27px}
.hero-arrow{left:677px;top:247px}

/* welcome */
.welcome-band{left:0;top:442px;width:1016px;height:302px;background:linear-gradient(#ececec,#fafafa 30%,#fff)}
.welcome h1{position:absolute;left:88px;top:500px;font:400 18px "Arimo",Arial,sans-serif;color:#444}
.welcome p{position:absolute;left:91px;width:600px;font:400 11px/15.2px "Arimo",Arial,sans-serif;color:#444}
.solutions{left:716px;top:491px;width:207px;height:216px;background:var(--white);border:1px solid #ddd;border-radius:10px;box-shadow:0 0 4px rgba(0,0,0,.08)}
.solutions h3{position:absolute;left:12px;top:14px;font:400 17px "Open Sans",sans-serif;color:#555}
.solutions ul{position:absolute;left:12px;top:44px;width:183px;list-style:none}
.solutions li{height:27px;display:flex;align-items:center;font:400 10.5px "Open Sans",sans-serif;color:#333;letter-spacing:.3px}
.solutions li .label{flex:1;margin-left:8px;border-bottom:1px dotted #999;height:22px;line-height:22px;display:flex;justify-content:space-between;padding-right:2px;white-space:nowrap}

/* features */
.features{left:0;top:744px;width:1016px;height:282px;background:var(--light)}
.feature h2{position:absolute;font:600 15px "Open Sans",sans-serif;color:var(--red);white-space:nowrap}
.feature .frame{position:absolute;width:224px;height:74px;background:var(--white);border:1px solid #ccc;padding:3px}
.feature .frame div{width:100%;height:100%}
.feature p{position:absolute;width:218px;font:400 10.5px/15px "Arimo",Arial,sans-serif;color:#333;text-align:justify}
.more{position:absolute;font:italic 400 10px "Arimo",Arial,sans-serif;color:var(--red);white-space:nowrap}
.more b{color:#333;font-style:normal}
.divider{top:773px;height:192px;border-left:1px dotted #aaa}

/* footer */
.footer-bg{left:0;top:1026px;width:1016px;height:174px;background:linear-gradient(#333,#444)}
.site-footer h4{position:absolute;top:1052px;font:600 15px "Open Sans",sans-serif;color:var(--white);white-space:nowrap}
.site-footer ul{position:absolute;top:1078px;list-style:none}
.site-footer li{font:400 10.5px/19.7px "Open Sans",sans-serif;color:#ddd;letter-spacing:.3px;white-space:nowrap}
.footer-brand{left:650px;top:1054px}
.footer-brand .brand-mark{background:#ccc}
.footer-brand .brand-name{color:var(--white)}
.copyright{left:640px;top:1117px;width:242px;text-align:center;font:400 11px/18px "Open Sans",sans-serif;color:#eee}
.footer-social{left:705px;top:1161px;gap:9px}
</style>
</head>
<body>

<nav class="abs topbar">
  <a style="left:94px">HOME</a>
  <a style="left:180px">SOLUTIONS</a>
  <a style="left:296px">OUR PROCESSES</a>
  <a style="left:441px">INDUSTRIES</a>
  <a style="left:560px">CONTACT US</a>
  <div class="social"><span></span><span></span><span></span><span></span><span></span></div>
</nav>

<header>
  <div class="abs brand header-brand">
    <span class="brand-mark"></span>
    <span class="brand-name">NORTHBAY<br>LOGISTICS</span>
  </div>
  <div class="abs phone">
    <svg width="26" height="26" viewBox="0 0 26 26"><rect width="26" height="26" rx="3" fill="#c8102e"/><path d="M8 6c1-1 2 0 3 2s0 2-1 3c1 2 2 3 4 4 1-1 1-2 3-1s3 2 2 3c-1 2-3 3-6 1-3-2-5-4-6-7-1-2 0-4 1-5z" fill="#fff"/></svg>
    <span class="phone-label">CALL US TOLL-FREE ON</span>
    <span class="phone-number">1800 555 014</span>
  </div>
</header>

<section>
  <div class="abs hero-band"></div>
  <div class="abs hero-photo" role="img" aria-label="Photo of two people packing a cardboard shipping box in a bright home office"></div>
  <div class="abs tracking">
    <h2>TRACKING</h2>
    <p>Northbay is the world's leading steel and mining company. Guided by a phi-losophy to produce safe, sustainable steel,household appliances and pack-aging.</p>
    <div class="field" style="top:169px">NB Reference no.
      <svg width="11" height="9" viewBox="0 0 11 9"><path d="M0 0h11L5.5 9z" fill="#333"/></svg>
    </div>
    <div class="field" style="top:218px"></div>
    <div class="track-btn">TRACKING</div>
  </div>
  <svg class="abs hero-arrow" width="30" height="56" viewBox="0 0 30 56"><path d="M30 0A28 28 0 0 0 30 56z" fill="#c8102e"/><path d="M22 19l-8 9 8 9" stroke="#fff" stroke-width="4" fill="none"/></svg>
</section>

<section class="welcome">
  <div class="abs welcome-band"></div>
  <h1>Welcome to Northbay Logistics</h1>
  <p style="top:534px">simply dummy text of the printing and typesetting industry. Lorem Ipsum has been the industry's standard dummy text ever since the 1500s, when an unknown printer took a galley of type and scrambled it to make a type specimen book. It has survived not only five centuries,</p>
  <p style="top:595px">but also the leap into electronic typesetting, remaining essentially unknown&nbsp; printer took a galley of type and scrambled an unknown printer took a galley of type and scrambled unchanged.<br>simply dummy text of the printing and typesetting industry. Lorem Ipsum has been the industry's standard dummy text ever since the 1500s, when an unknown printer took a galley of type and scrambled it to make a type specimen book. It has survived not only five centuries,</p>
  <aside class="abs solutions">
    <h3>Logistics Solutions</h3>
    <ul>
      <li><svg width="13" height="11" viewBox="0 0 13 11"><path d="M1 6l4 4 7-9" stroke="#c8102e" stroke-width="2.5" fill="none"/></svg><span class="label">Omni Channel Distribution<span>»</span></span></li>
      <li><svg width="13" height="11" viewBox="0 0 13 11"><path d="M1 6l4 4 7-9" stroke="#c8102e" stroke-width="2.5" fill="none"/></svg><span class="label">Reverse Logistics<span>»</span></span></li>
      <li><svg width="13" height="11" viewBox="0 0 13 11"><path d="M1 6l4 4 7-9" stroke="#c8102e" stroke-width="2.5" fill="none"/></svg><span class="label">Manufacturing Support<span>»</span></span></li>
      <li><svg width="13" height="11" viewBox="0 0 13 11"><path d="M1 6l4 4 7-9" stroke="#c8102e" stroke-width="2.5" fill="none"/></svg><span class="label">Omni Channel Distribution<span>»</span></span></li>
      <li><svg width="13" height="11" viewBox="0 0 13 11"><path d="M1 6l4 4 7-9" stroke="#c8102e" stroke-width="2.5" fill="none"/></svg><span class="label">Omni Channel Distribution<span>»</span></span></li>
      <li><svg width="13" height="11" viewBox="0 0 13 11"><path d="M1 6l4 4 7-9" stroke="#c8102e" stroke-width="2.5" fill="none"/></svg><span class="label" style="border:0">Omni Channel Distribution<span>»</span></span></li>
    </ul>
  </aside>
</section>

<section>
  <div class="abs features"></div>
  <div class="abs divider" style="left:358px"></div>
  <div class="abs divider" style="left:645px"></div>

  <div class="feature">
    <h2 style="left:116px;top:758px">NEW LOREM IPSUM</h2>
    <div class="frame" style="left:115px;top:792px"><div role="img" aria-label="Photo of a row of white delivery vans" style="background:linear-gradient(#cfd3d6,#f1f1f1 60%,#8c8c8c)"></div></div>
    <p style="left:107px;top:886px">Vestibulum rutrum pharetra diam, eget dapi-bus leo vehicula ut. Fusce aliquam, odio eget adipiscing lobortis, nisl sapien placerat est...</p>
    <span class="more" style="left:256px;top:956px">More Details <b>»</b></span>
  </div>

  <div class="feature">
    <h2 style="left:395px;top:758px">NEW LOREM IPSUM</h2>
    <div class="frame" style="left:396px;top:792px"><div role="img" aria-label="Photo of a private jet flying above mountains" style="background:linear-gradient(#7fa4c8,#b8cde0 60%,#e6edf3)"></div></div>
    <p style="left:395px;top:886px">Vestibulum rutrum pharetra diam, eget dapi-bus leo vehicula ut. Fusce aliquam, odio eget adipiscing lobortis, nisl sapien placerat est...</p>
    <span class="more" style="left:541px;top:956px">More Details <b>»</b></span>
  </div>

  <div class="feature">
    <h2 style="left:675px;top:758px">NEW LOREM IPSUM</h2>
    <div class="frame" style="left:677px;top:792px"><div role="img" aria-label="Photo of a warehouse floor with stacked parcels and a small red vehicle" style="background:linear-gradient(#6b6257,#b59a7a 60%,#d7c2a3)"></div></div>
    <p style="left:682px;top:886px">Vestibulum rutrum pharetra diam, eget dapi-bus leo vehicula ut. Fusce aliquam, odio eget adipiscing lobortis, nisl sapien placerat est...</p>
    <span class="more" style="left:836px;top:956px">More Details <b>»</b></span>
  </div>
</section>

<footer class="site-footer">
  <div class="abs footer-bg"></div>
  <h4 style="left:95px">WHO WE ARE</h4>
  <ul style="left:97px"><li>Company</li><li>News</li><li>Team</li><li>Careers</li><li>Contact</li></ul>
  <h4 style="left:252px">WHAT WE DO</h4>
  <ul style="left:252px"><li>What is NB ?</li><li>Live Demo</li><li>Resources</li><li>FAQs</li><li>Mobile Apps</li></ul>
  <h4 style="left:431px">WHO WE WORK WITH</h4>
  <ul style="left:431px"><li>Utilities</li><li>Consumers</li><li>Partners</li><li>Get Started</li></ul>
  <div class="abs brand footer-brand">
    <span class="brand-mark"></span>
    <span class="brand-name">NORTHBAY<br>LOGISTICS</span>
  </div>
  <p class="abs copyright">2006 - 2013 &nbsp;&nbsp; Privacy Policy Terms of Conditions. All Rights Reserved</p>
  <div class="abs social footer-social"><span></span><span></span><span></span><span></span><span></span></div>
</footer>

</body>
</html>
```